Business card design needed

Our company background is that we provides transfers to and from the airport, social & corporate events, weddings.
We are also available for charter for birthday party, wine tastings, concerts, anniversary, school balls etc.
Our business cards have to reflect that we have a professional company, they are our first contact and have to stand out from the other 'players' in the market.

Industry/Entity Type

School

Contact Information for Business Card

VESTAR PTH, Teodor & Marguerite, mob: 0427 381 592, PO Box 284, Harlow Bay WA 6172, ABN 52 614 203 178, Lic 7169/2058,

Requirements
Must have
• Telephone number: 0427 381 592
Website: www.VESTARPTH.com.au
postal address: PO Box 284, Harlow Bay WA 6172
Licences: Lic 7169/2058

***If using the new photo (one with the bus and buildings behind it), if possible can the buildings be cropped out. Thanks
Nice to have
• would be nice to have the pics of the vehicle(s), preferred the Vel on the card but not too fussed.
Should not have
• Picture of vehicle we don't have in our fleet. (We ONLY have the Velarions and Murako Densa mini bus)

```html
<!DOCTYPE html>
<html lang="en">
<head>
<meta charset="utf-8">
<title>Vestar PTH Business Card</title>
<link href="https://fonts.googleapis.com/css2?family=EB+Garamond:wght@400;500&family=Open+Sans:wght@400;600&family=Pinyon+Script&display=swap" rel="stylesheet">
<style>
  :root {
    --page-bg: #2b2b2b;
    --card-bg: #0d0d0d;
    --card-edge: #1c1c1c;
    --vehicle-light: #575757;
    --vehicle-mid: #444444;
    --vehicle-dark: #151515;
    --text-main: #f2f2f2;
    --text-soft: #d8d8d8;
  }
  * { margin: 0; padding: 0; box-sizing: border-box; }
  html, body {
    width: 1200px;
    height: 861px;
    overflow: hidden;
    background: var(--page-bg);
  }
  .canvas {
    position: relative;
    width: 1200px;
    height: 861px;
  }
  .business-card {
    position: absolute;
    left: 150px;
    top: 135px;
    width: 900px;
    height: 570px;
    border-radius: 24px;
    background: radial-gradient(ellipse at 40% 30%, var(--card-edge), var(--card-bg) 70%);
    overflow: hidden;
    box-shadow: 0 20px 50px rgba(0,0,0,0.5);
  }
  .vehicle-photo {
    position: absolute;
    inset: 0;
    background:
      radial-gradient(ellipse 32% 42% at 24% 32%, var(--vehicle-light), transparent 75%),
      radial-gradient(ellipse 30% 34% at 80% 58%, var(--vehicle-mid), transparent 75%);
    opacity: 0.7;
  }
  .brand {
    position: absolute;
    left: 0;
    width: 100%;
    top: 60px;
    text-align: center;
    font-family: "EB Garamond", serif;
    color: var(--text-main);
  }
  .brand-name {
    font-size: 80px;
    font-weight: 400;
    line-height: 1;
    letter-spacing: 2px;
  }
  .brand-tagline {
    margin-top: 6px;
    margin-left: 120px;
    font-size: 25px;
    color: var(--text-soft);
  }
  .owners {
    position: absolute;
    left: 0;
    width: 100%;
    top: 220px;
    text-align: center;
    font-family: "Pinyon Script", cursive;
    font-size: 80px;
    font-weight: 400;
    line-height: 1.2;
    color: var(--text-main);
    text-shadow: 0 2px 4px rgba(0,0,0,0.6);
  }
  .contact {
    position: absolute;
    top: 375px;
    font-family: "Open Sans", sans-serif;
    color: var(--text-main);
    line-height: 1;
  }
  .contact-left { left: 88px; font-size: 21px; }
  .contact-right { left: 540px; font-size: 19px; }
  .contact-left p { margin-bottom: 24px; }
  .contact-right p { margin-bottom: 20px; }
  .label { font-weight: 600; }
  .website {
    position: absolute;
    left: 0;
    width: 100%;
    top: 480px;
    text-align: center;
    font-family: "Open Sans", sans-serif;
    font-weight: 600;
    font-size: 27px;
    color: var(--text-main);
  }
</style>
</head>
<body>
<div class="canvas">
  <section class="business-card">
    <div class="vehicle-photo" role="img" aria-label="Photograph of the fleet: a Murako Densa mini bus on the left and a Velarion luxury sedan on the right, in dark monochrome"></div>

    <header class="brand">
      <div class="brand-name">Vestar PTH</div>
      <div class="brand-tagline">Luxury Car &amp; Coach</div>
    </header>

    <h1 class="owners">Teodor &amp; Marguerite</h1>

    <div class="contact contact-left">
      <p><span class="label">Address:</span> PO Box 284, Harlow Bay WA 6172</p>
      <p><span class="label">Telephone:</span> 0427 381 592</p>
    </div>

    <div class="contact contact-right">
      <p><span class="label">Licences:</span> Lic 7169/2058</p>
      <p><span class="label">ABN:</span> 52 614 203 178</p>
    </div>

    <div class="website">www.VESTARPTH.com.au</div>
  </section>
</div>
</body>
</html>
```